Adult Store requires exciting banner ad designs for online store

Marlo Tide requires an online estore homepage design template for slider ads, banner ads designs, collection ad designs, product specific ad design - based on current brand theme featuring sexy fun inked up girls & and guys and build on the australia bondi beach location.
Our current tagline is 'Time For A New Vibe?'
The ad design specs should be based on normal website design specs
www.marlotide.com

Target Market(s)

Women and men 18-35 shopping online for a new adult toys
Shoppers looking for something different in the category
Pregnant females looking for sex toys

Font styles to use
Sans Serif

Colors

Designer to choose colors to be used in the design.

Requirements
Must have
• * Build on the worldwide popularity of the Bondi beach location
• Must include company logo with tag line
• * Must include website address
• * Sex Toys Factory outlet clearance Sale or Sex toys clearance sale
• * WORLDWIDE SAME DAY SHIPPING x 7-Days (or your variation)
• * Include inked up girl image or guru
• * Has a call to action (Click me etc)
• * Attention grabbing, fun & exciting yet still professional
• * Include tasteful images that shoppers want to be like
• * Promotes only a visitor who is interested to click
• * Include somewhere 'Proudly Australian Owned & Operated logo'
• * Include reference to hens / bucks parties
• * Looking for your own creative flair, be original !!
Nice to have
• Subtle inked up tattoo theme, images of sexy young seductive inked up girls and guys, gay and straight.
Should not have
• Images or text deemed offensive
• Ads and background should not have overly Dark repressive colours

```html
<!DOCTYPE html>
<html lang="en">
<head>
<meta charset="utf-8">
<title>Marlo Tide – Factory Clearance Banners</title>
<link rel="stylesheet" href="https://fonts.googleapis.com/css2?family=Raleway:wght@300;400;700;800&family=Great+Vibes&family=Caveat:wght@400&display=swap">
<style>
  :root {
    --blue: #5487e8;
    --magenta: #e044ee;
    --paper: #f4f4f4;
    --ink: #1d1d1d;
    --white: #ffffff;
    --photo-dark: #6f6a6c;
    --photo-light: #d9d2cf;
    --body-font: "Raleway", sans-serif;
    --script-font: "Great Vibes", cursive;
    --marker-font: "Caveat", cursive;
  }
  * { box-sizing: border-box; margin: 0; padding: 0; }
  html, body { width: 1200px; height: 450px; overflow: hidden; background: var(--white); }
  body { font-family: var(--body-font); }

  .canvas { position: relative; width: 1200px; height: 450px; }

  .banner { position: absolute; top: 0; height: 450px; overflow: hidden; background: var(--paper); }
  .banner--landscape { left: 0; width: 555px; }
  .banner--feature { left: 661px; width: 539px; }

  .banner__shapes { position: absolute; inset: 0; width: 100%; height: 100%; }

  .photo {
    position: absolute;
    background: linear-gradient(160deg, var(--photo-light) 0%, #a89a96 45%, var(--photo-dark) 100%);
    border-radius: 40px 40px 0 0;
  }
  .banner--landscape .photo { left: 40px; top: 0; width: 295px; height: 275px; border-radius: 0 0 60px 0; }
  .banner--feature .photo { left: 210px; top: 205px; width: 320px; height: 245px; }

  .brand-mark {
    position: absolute; display: flex; align-items: center; gap: 4px;
    font-family: var(--body-font); font-weight: 700; font-size: 10px; color: var(--ink);
  }
  .brand-mark__dot { width: 12px; height: 12px; border-radius: 50%; background: var(--ink); }
  .banner--landscape .brand-mark { left: 6px; top: 24px; }
  .banner--feature .brand-mark { right: 6px; top: 24px; }

  .origin-badge { position: absolute; width: 46px; height: 40px; }
  .banner--landscape .origin-badge { left: 500px; top: 398px; }
  .banner--feature .origin-badge { left: 32px; top: 8px; }

  .headline-script {
    position: absolute; left: 300px; top: 30px; width: 240px;
    font-family: var(--script-font); font-size: 40px; line-height: 46px;
    text-align: center; color: var(--ink);
  }
  .offer {
    position: absolute; left: 330px; top: 176px; width: 180px;
    font-weight: 300; font-size: 19px; line-height: 23px; letter-spacing: 1.5px;
    text-align: center; color: var(--ink);
  }

  .btn {
    position: absolute; display: flex; align-items: center; justify-content: center;
    font-weight: 800; font-size: 10.5px; letter-spacing: 1px; color: var(--white);
    border-radius: 8px; text-decoration: none;
  }
  .btn--solid { width: 78px; height: 27px; background: linear-gradient(135deg, var(--blue) 0%, var(--blue) 45%, var(--magenta) 46%, #a35cf0 100%); }
  .btn--outline { width: 78px; height: 26px; border: 2.5px solid var(--white); background: transparent; }
  .banner--landscape .btn--solid { left: 381px; top: 244px; }
  .banner--landscape .btn--outline { left: 80px; top: 362px; }
  .banner--feature .btn--outline { left: 139px; top: 197px; }
  .banner--feature .btn--solid { left: 385px; top: 196px; }

  .clearance-script {
    position: absolute; left: 18px; top: 214px;
    font-family: var(--script-font); font-size: 30px; line-height: 38px; color: var(--white);
  }
  .product { position: absolute; font-size: 13.5px; line-height: 20px; letter-spacing: 0.6px; color: var(--white); }
  .banner--landscape .product { left: 19px; top: 296px; }
  .banner--feature .product { left: 60px; top: 116px; width: 240px; text-align: center; font-size: 13px; }

  .shipping-line {
    position: absolute; left: 98px; top: 429px; display: flex; align-items: center; gap: 6px;
    font-size: 11px; color: var(--white);
  }
  .shipping-icon { width: 20px; height: 20px; }
  .web-address { position: absolute; font-size: 11px; letter-spacing: 0.3px; color: var(--white); }
  .banner--landscape .web-address { left: 348px; top: 434px; }
  .banner--feature .web-address { left: 23px; top: 434px; }

  .clearance-marker {
    position: absolute; left: 80px; top: 18px; width: 200px;
    font-family: var(--marker-font); font-size: 22px; line-height: 27px; letter-spacing: 5px;
    text-transform: uppercase; text-align: center; color: var(--white);
  }
  .tagline-marker {
    position: absolute; left: 318px; top: 76px; width: 210px;
    font-family: var(--marker-font); font-size: 30px; line-height: 36px; letter-spacing: 5px;
    text-transform: uppercase; text-align: center; color: var(--magenta);
    text-shadow: 0 0 6px rgba(224, 68, 238, 0.45);
  }
  .shipping-block {
    position: absolute; left: 0; top: 228px; width: 124px;
    display: flex; flex-direction: column; align-items: center; gap: 6px;
    font-size: 18px; line-height: 27px; text-align: center; color: var(--white);
  }
  .shipping-block .shipping-icon { width: 40px; height: 40px; }
</style>
</head>
<body>
<main class="canvas">

  <!-- Landscape banner -->
  <section class="banner banner--landscape" aria-label="Factory clearance banner, landscape">
    <div class="photo" role="img" aria-label="Photo of a tattooed woman with silver hair resting her head on her arm"></div>
    <svg class="banner__shapes" viewBox="0 0 555 450" aria-hidden="true">
      <polygon points="0,139 444,315 0,450" fill="var(--blue)"/>
      <polygon points="0,450 555,283 555,450" fill="var(--magenta)"/>
      <line x1="0" y1="450" x2="444" y2="316" stroke="var(--white)" stroke-width="2"/>
    </svg>

    <div class="brand-mark"><span class="brand-mark__dot"></span>Marlo Tide</div>

    <h1 class="headline-script">Its Time<br>For a<br>New Vibe</h1>
    <p class="offer">Up to 60% off selected items</p>
    <a class="btn btn--solid" href="#">SHOP ALL</a>

    <h2 class="clearance-script">Sex Toy Factory<br>Clearance</h2>
    <p class="product">The Automatic Sex MAchine Gun<br>With a Bonus Carry Bag<br>149$</p>
    <a class="btn btn--outline" href="#">SHOP NOW</a>

    <p class="shipping-line">
      <svg class="shipping-icon" viewBox="0 0 40 40" aria-hidden="true" fill="none" stroke="var(--white)" stroke-width="2">
        <circle cx="18" cy="22" r="14"/><path d="M4 22h28M18 8c-6 8-6 20 0 28M18 8c6 8 6 20 0 28"/>
        <rect x="22" y="3" width="14" height="12" fill="var(--magenta)"/>
      </svg>
      Same day worldwide shipping
    </p>
    <p class="web-address">www.marlotide.com</p>
    <svg class="origin-badge" viewBox="0 0 46 40" aria-hidden="true"><polygon points="23,0 46,40 0,40" fill="#f6d9fa"/></svg>
  </section>

  <!-- Feature banner -->
  <section class="banner banner--feature" aria-label="Factory clearance banner, feature">
    <svg class="banner__shapes" viewBox="0 0 539 450" aria-hidden="true">
      <polygon points="0,0 5,0 208,450 0,450" fill="var(--blue)"/>
      <polygon points="12,0 371,0 165,357" fill="var(--magenta)"/>
      <line x1="5" y1="0" x2="208" y2="450" stroke="var(--white)" stroke-width="3"/>
    </svg>
    <div class="photo" role="img" aria-label="Photo of a tattooed woman with silver hair leaning on her arm"></div>

    <svg class="origin-badge" viewBox="0 0 46 40" aria-hidden="true"><polygon points="23,0 46,40 0,40" fill="#f6d9fa"/></svg>
    <h2 class="clearance-marker">Sex Toy<br>Factory<br>Clearance</h2>
    <p class="product">The Automatic Sex MAchine Gun<br>With a Bonus Carry Bag<br>149$</p>
    <a class="btn btn--outline" href="#">SHOP NOW</a>

    <div class="brand-mark"><span class="brand-mark__dot"></span>Marlo Tide</div>
    <h1 class="tagline-marker">Its Time<br>For a<br>New Vibe</h1>
    <a class="btn btn--solid" href="#">SHOP ALL</a>

    <div class="shipping-block">
      <svg class="shipping-icon" viewBox="0 0 40 40" aria-hidden="true" fill="none" stroke="var(--white)" stroke-width="2">
        <circle cx="18" cy="22" r="14"/><path d="M4 22h28M18 8c-6 8-6 20 0 28M18 8c6 8 6 20 0 28"/>
        <rect x="22" y="3" width="14" height="12" fill="var(--blue)"/>
      </svg>
      <p>Same day<br>worldwide<br>shipping</p>
    </div>
    <p class="web-address">www.marlotide.com</p>
  </section>

</main>
</body>
</html>
```